Moder Business Card Design for Renewables Business

Need a business card design for my business. We collect & repurpose spent coffee ground from cafes. The cards will be made from recycled paper. Needs to fit our corporate colour scheme of white, green & brown (see logo for colour codes). Eco friendly, modern, intresting & eye catching.
This card needs to convey the message of the business and fit into its mantra of eco-friendly, sustainable etc.

Target Market(s)

Cafe Owners, Coffee Drinkers, Recycling Companies, Farmers

Industry/Entity Type

Recycling

Contact Information for Business Card

Name; Peter Halloran
Phone; 0412 386 527
e-mail; info@lumatrove.com.au
website; www.lumatrove.com.au

Font styles to use
Sans Serif
Script

Colors

Designer to choose colors to be used in the design.

Requirements
Must have
• FRONT;
• Logo, Name (Peter Halloran), phone number, e-mail address, website
• BACK;
• On the back in cursive text; 'SECOND LIFE FOR EVERY COFFEE GROUND'
• Small facebook & Instagram logos with text 'Lumatrove'
Should not have
• messy design

```html
<!DOCTYPE html>
<html lang="en">
<head>
<meta charset="utf-8">
<title>Lumatrove Business Card</title>
<link href="https://fonts.googleapis.com/css2?family=Open+Sans:wght@400;600&family=Pinyon+Script&family=Great+Vibes&display=swap" rel="stylesheet">
<style>
  :root {
    --brown: #52200a;
    --green: #66cc00;
    --ink: #111111;
    --paper: #ffffff;
  }
  html, body {
    margin: 0;
    padding: 0;
    width: 1030px;
    height: 1200px;
    overflow: hidden;
    background: var(--paper);
  }
  .canvas {
    position: relative;
    width: 1030px;
    height: 1200px;
    font-family: "Open Sans", Arial, sans-serif;
  }
  .rule { position: absolute; }
  .rule--brown { background: var(--brown); }
  .rule--green { background: var(--green); }
  .rule--ink { background: var(--ink); }

  /* Brand lockup */
  .brand-lockup {
    position: absolute;
    display: flex;
    align-items: center;
    gap: 12px;
  }
  .brand-dot {
    width: 30px;
    height: 30px;
    border-radius: 50%;
    background: var(--green);
  }
  .brand-name {
    font-family: "Open Sans", Arial, sans-serif;
    font-weight: 600;
    color: var(--brown);
    letter-spacing: 0.5px;
    line-height: 1;
  }

  /* Front */
  .front .brand-lockup { left: 92px; top: 374px; }
  .front .brand-name { font-size: 36px; }

  .holder-name {
    position: absolute;
    left: 387px;
    top: 150px;
    margin: 0;
    font-family: "Pinyon Script", cursive;
    font-weight: 400;
    font-size: 92px;
    line-height: 1;
    color: var(--brown);
    white-space: nowrap;
  }
  .contact {
    position: absolute;
    left: 445px;
    top: 268px;
    margin: 0;
    font-size: 25px;
    line-height: 39px;
    color: var(--ink);
    display: grid;
    grid-template-columns: 128px 25px auto;
  }
  .contact dt, .contact dd { margin: 0; }

  /* Back */
  .back .brand-lockup { left: 50%; top: 836px; transform: translateX(-50%); }
  .back .brand-name { font-size: 44px; }
  .tagline {
    position: absolute;
    left: 170px;
    width: 680px;
    top: 1008px;
    margin: 0;
    text-align: center;
    font-family: "Great Vibes", cursive;
    font-weight: 400;
    font-size: 52px;
    line-height: 1.1;
    color: var(--ink);
    white-space: nowrap;
  }
  .social {
    position: absolute;
    left: 380px;
    top: 1100px;
    display: flex;
    align-items: center;
    gap: 10px;
    font-size: 29px;
    line-height: 1;
    color: var(--ink);
  }
  .social-mark {
    width: 22px;
    height: 22px;
    background: var(--ink);
  }
</style>
</head>
<body>
<main class="canvas">

  <section class="card front" aria-label="Card front">
    <div class="rule rule--brown" style="left:184px; top:48px; width:788px; height:4px;"></div>
    <div class="rule rule--brown" style="left:967px; top:48px; width:5px; height:365px;"></div>
    <div class="rule rule--green" style="left:77px; top:121px; width:4px; height:416px;"></div>
    <div class="rule rule--green" style="left:77px; top:533px; width:655px; height:4px;"></div>

    <div class="brand-lockup">
      <span class="brand-dot"></span>
      <span class="brand-name">LUMATROVE</span>
    </div>

    <h1 class="holder-name">Peter Halloran</h1>

    <dl class="contact">
      <dt>Phone</dt><dd>:</dd><dd>0412 386 527</dd>
      <dt>e-mail</dt><dd>:</dd><dd>info@lumatrove.com.au</dd>
      <dt>website</dt><dd>:</dd><dd>www.lumatrove.com.au</dd>
    </dl>
  </section>

  <section class="card back" aria-label="Card back">
    <div class="rule rule--brown" style="left:170px; top:667px; width:786px; height:4px;"></div>
    <div class="rule rule--brown" style="left:951px; top:667px; width:5px; height:416px;"></div>
    <div class="rule rule--green" style="left:61px; top:740px; width:4px; height:415px;"></div>
    <div class="rule rule--green" style="left:61px; top:1151px; width:800px; height:4px;"></div>

    <div class="brand-lockup">
      <span class="brand-dot"></span>
      <span class="brand-name">LUMATROVE</span>
    </div>

    <p class="tagline">Second Life For Every Coffee Ground</p>
    <div class="rule rule--ink" style="left:172px; top:1078px; width:676px; height:3px;"></div>

    <div class="social">
      <span class="social-mark"></span>
      <span>Lumatrove</span>
    </div>
  </section>

</main>
</body>
</html>
```